Business card design for online Mandarin Learning School

We need a business card design for our online language learning school called "Maple Bridge Online for Mandarin Learning". Our existing website is https://www.maplebridgeonline.com
We have our logo already. We would like to see our business card design that can make our online teaching services to be innovative, young, energetic and fun to learn. Prefer to have a certain level of color matching with our website. Apart from "Maple Bridge Online", need to specifically state "for Mandarin Learning" as well on the business card.

```html
<!DOCTYPE html>
<html lang="en">
<head>
<meta charset="utf-8">
<title>Maple Bridge Online for Mandarin Learning – Business Card</title>
<link rel="stylesheet" href="https://fonts.googleapis.com/css2?family=Cinzel:wght@400&family=Oswald:wght@500&family=Lato:wght@400;700&display=swap">
<style>
  :root {
    --canvas-bg: #bcbcbc;
    --teal: #1ba6ae;
    --teal-deep: #12878f;
    --coral: #f47c6b;
    --sun: #ffd166;
    --ink: #5f6165;
    --faint-teal: #dff3f5;
    --faint-pink: #fde6e6;
    --white: #ffffff;
  }
  * { box-sizing: border-box; margin: 0; padding: 0; }
  html, body {
    width: 1200px; height: 930px; overflow: hidden;
    background: var(--canvas-bg);
  }
  .canvas { position: relative; width: 1200px; height: 930px; }
  .card {
    position: absolute; width: 520px; height: 300px;
    border-radius: 22px; overflow: hidden;
    box-shadow: 0 6px 16px rgba(0,0,0,.18);
  }
  .card-front {
    left: 100px; top: 110px;
    background: linear-gradient(135deg, var(--teal) 0%, var(--teal-deep) 100%);
  }
  .card-back { left: 580px; top: 500px; background: var(--white); }

  .front-accent {
    position: absolute; left: 0; right: 0; bottom: 0; height: 10px;
    background: linear-gradient(90deg, var(--coral), var(--sun));
  }
  .front-mark {
    position: absolute; left: 0; right: 0; top: 82px;
    display: flex; flex-direction: column; align-items: center;
  }
  .front-dot { width: 34px; height: 34px; border-radius: 50%; background: var(--coral); }
  .front-name {
    margin-top: 18px;
    font-family: "Cinzel", serif; font-size: 38px; letter-spacing: 1px;
    color: var(--white); line-height: 1.2;
  }
  .front-tagline {
    margin-top: 6px;
    font-family: "Lato", sans-serif; font-weight: 700; font-size: 16px;
    letter-spacing: 3px; text-transform: uppercase; color: var(--sun);
  }

  .back-watermark {
    position: absolute; left: 210px; top: 70px; width: 190px; height: 190px;
    border-radius: 50%;
    background: linear-gradient(160deg, var(--faint-pink) 0%, var(--faint-teal) 70%);
  }
  .back-accent {
    position: absolute; left: 0; top: 0; bottom: 0; width: 10px;
    background: linear-gradient(180deg, var(--coral), var(--sun));
  }
  .person {
    position: absolute; left: 0; top: 132px; width: 246px; text-align: right;
  }
  .person-name {
    font-family: "Oswald", sans-serif; font-weight: 500; font-size: 32px;
    color: var(--teal); letter-spacing: .5px; line-height: 1.1;
  }
  .person-role {
    font-family: "Lato", sans-serif; font-size: 14px; color: var(--coral);
    margin-top: 2px;
  }
  .divider {
    position: absolute; left: 258px; top: 112px; width: 1px; height: 76px;
    background: var(--teal);
  }
  .contacts {
    position: absolute; left: 270px; top: 108px; list-style: none;
    font-family: "Lato", sans-serif; font-size: 15px; color: var(--ink);
  }
  .contacts li { display: flex; align-items: center; gap: 8px; height: 24px; }
  .contacts svg { width: 12px; height: 12px; flex: none; }
  .address {
    position: absolute; left: 0; right: 0; top: 246px; text-align: center;
    font-family: "Lato", sans-serif; font-size: 15px; color: var(--ink);
  }
</style>
</head>
<body>
<main class="canvas">
  <section class="card card-front" aria-label="Card front">
    <div class="front-mark">
      <span class="front-dot"></span>
      <span class="front-name">MAPLE BRIDGE</span>
      <span class="front-tagline">for Mandarin Learning</span>
    </div>
    <span class="front-accent"></span>
  </section>

  <section class="card card-back" aria-label="Card back">
    <span class="back-accent"></span>
    <div class="back-watermark" role="img" aria-label="Faint brand emblem area"></div>
    <div class="person">
      <p class="person-name">DANA WHITFIELD</p>
      <p class="person-role">Director</p>
    </div>
    <span class="divider"></span>
    <ul class="contacts">
      <li>
        <svg viewBox="0 0 12 12"><path d="M2.5 1l2 2.2-1 1.3a6 6 0 0 0 4 4l1.3-1 2.2 2-1.3 1.5C5.5 11 1 6.5 1 2.3z" fill="#1ba6ae"/></svg>
        +330 2460-5173
      </li>
      <li>
        <svg viewBox="0 0 12 12"><rect x="1" y="2.5" width="10" height="7" fill="none" stroke="#1ba6ae" stroke-width="1.2"/><path d="M1 2.5l5 4 5-4" fill="none" stroke="#1ba6ae" stroke-width="1.2"/></svg>
        info@maplebridgeonline.com
      </li>
      <li>
        <svg viewBox="0 0 12 12"><circle cx="6" cy="6" r="5" fill="none" stroke="#1ba6ae" stroke-width="1.2"/><path d="M1 6h10M6 1c-2.5 3-2.5 7 0 10M6 1c2.5 3 2.5 7 0 10" fill="none" stroke="#1ba6ae" stroke-width="1"/></svg>
        www.maplebridgeonline.com
      </li>
    </ul>
    <p class="address">2780 Alder Lane Ridgeway, MT 59310</p>
  </section>
</main>
</body>
</html>
```